Front, spine and back covers for new textbook "Summit Blueprints"

Create a design for the front and back cover page of my new book "Summit Blueprints" that has elements of the cover of my existing textbook "Horizon Tactics" (see Quillmart.com or attached files), such that it looks like a book from the same company (Brindlex) but distinct enough for it to be clearly recognized by readers as a brand-new book on a brand-new topic. "Horizon Tactics" is about the best practices for scheduling projects, whereas the new book "Summit Blueprints" is about the best practices for scheduling programs: 'A program is a set of related projects that are better managed together than apart'. In other words: A program is a really BIG project, so big it needs to be subdivided into multiple projects and then integrated again with cross-project dependencies (normally depicted with arrows!) in order to keep the overview over the entire program.
Updates

Reason: Some more designs were submitted or refined at my request. Please submit them, so I can involve them in a survey among my technical editors...

Target Market(s)

program managers, subproject managers and program support staff

Font styles to use
Sans Serif

Colors

Designer to choose colors to be used in the design.

Requirements
Must have
• The cover of the book must be size: 19 cm wide * 23.5 cm high (7.5 * 9.25 inch); the thickness of the book varies with the number of pages in the book currently estimated at 250 pages.
• (Draft) Title: Summit Blueprints
• (Draft) Subtitle: Best Practices for Scheduling Real-World Programs
• (Draft) Sub-subtitle: Screenshots in Ganttwise Studio
• The design must include front cover, spine cover and back cover.
• The exact text will be provided for the front back, spine cover and back cover.
• Must 'feel' like a book from the same company that published the book "Horizon Tactics", but the design must be distinct enough to be clearly recognized by potential readers as a brand-new book on a brand-new topic.
• Appear as a textbook for professionals, for the business community
• Design files must be native Microsoft Windows computer application files that author can further refine and edit with appropriate Microsoft Windows-based design software, like the Adobe or Corel suite.
• Copyrights must be acknowledged.
Nice to have
• Somehow the audaciousness of a large undertaking like program should be reflected in the design.
• Somehow the 'leading edge' nature of the books contents needs to be reflected; there are very few books on 'program management'.
• Colors for taskbars in a Gantt Chart (=chart with tasks over time with durations of tasks depicted as bars) are often blue. The Critical Path (=series of tasks that drive the project duration) task bars are red. A program schedule has Gantt Charts and one (or more) Critical Path(s). Dependencies between activities in a project schedule or between subproject schedules are depicted as arrows.
Should not have
• Same design as "Horizon Tactics"
• Appear unprofessional

```html
<!DOCTYPE html>
<html lang="en">
<head>
<meta charset="utf-8">
<title>Summit Blueprints – Cover Spread</title>
<link rel="stylesheet" href="https://fonts.googleapis.com/css2?family=Oswald:wght@400;500&family=Roboto+Condensed:wght@400;700&display=swap">
<style>
  :root{
    --title-blue:#1b6cb4;
    --teal:#6ccbd9;
    --teal-deep:#4fb8c9;
    --label-yellow:#ffe27c;
    --play-orange:#f8b631;
    --magenta:#e5197e;
    --green:#69bd3a;
    --author-orange:#f28a1d;
    --ink:#1c1c1c;
    --shadow-gray:#d9dde0;
    --badge-gray:#c2c4c6;
    --paper:#ffffff;
  }
  *{box-sizing:border-box;margin:0;padding:0}
  html,body{width:1200px;height:693px;overflow:hidden;background:var(--paper)}
  .spread{position:relative;width:1200px;height:693px;overflow:hidden;background:var(--paper);font-family:"Oswald",sans-serif}
  .abs{position:absolute}

  /* back cover */
  .back-wave{left:0;top:0}
  .back-icon{left:42px;top:20px;width:120px;height:120px;border-radius:50%;
    background:radial-gradient(circle,#f4f8f9 0 38%,#a7dfe7 39% 100%)}
  .back-title{left:176px;top:18px;color:var(--title-blue);font-weight:400;font-size:44px;line-height:44px;letter-spacing:.5px}
  .back-play{left:180px;top:118px;width:42px;height:38px;background:var(--play-orange);border-radius:5px}
  .back-label{left:218px;top:120px;width:198px;height:46px;background:var(--label-yellow);box-shadow:5px 4px 0 var(--shadow-gray);padding:4px 6px}
  .back-label .sub{color:var(--magenta);font-size:13px;line-height:13px}
  .back-label .subsub{color:var(--green);font-size:11px;line-height:13px}
  .back-box{left:357px;top:577px;width:145px;height:75px;background:var(--badge-gray)}
  .brand{font-family:"Roboto Condensed",sans-serif;font-weight:700;color:var(--ink);display:flex;align-items:center;gap:6px}
  .brand .dot{width:16px;height:16px;border-radius:50%;background:var(--ink)}
  .back-brand{left:46px;top:604px;font-size:26px}

  /* spine */
  .spine{left:570px;top:0;width:66px;height:693px}
  .spine-text{position:absolute;left:66px;top:50px;transform-origin:0 0;transform:rotate(90deg);white-space:nowrap}
  .spine-title{color:var(--title-blue);font-size:36px;line-height:36px}
  .spine-sub{color:var(--magenta);font-size:14px;line-height:15px}
  .spine-sub span{color:var(--green);font-size:12px}
  .spine-author{color:var(--author-orange);font-size:14px;line-height:15px;font-weight:500}
  .spine-brand{position:absolute;left:42px;top:500px;transform-origin:0 0;transform:rotate(90deg);font-size:18px}
  .spine-badge{position:absolute;left:14px;top:600px;width:42px;height:62px;background:var(--badge-gray);border:3px solid #7f9fc0}

  /* front cover */
  .front-circle{left:636px;top:0}
  .front-title{left:672px;top:36px;color:var(--title-blue);font-size:96px;line-height:100px;letter-spacing:1px}
  .front-play{left:674px;top:245px;width:98px;height:88px;background:var(--play-orange);border-radius:10px;box-shadow:6px 8px 0 #f6a21d}
  .front-label{left:774px;top:245px;width:374px;height:106px;background:var(--label-yellow);box-shadow:8px 8px 0 var(--shadow-gray);padding:10px 12px}
  .front-label .sub{color:var(--magenta);font-size:25px;line-height:28px}
  .front-label .subsub{color:var(--green);font-size:21px;line-height:26px}
  .front-art{left:640px;top:376px;width:312px;height:254px;
    background:linear-gradient(135deg,#c9b98a 0%,#b7dfcf 40%,#bfe4ec 70%,#8fd2de 100%)}
  .front-credit{left:970px;top:478px;font-family:"Roboto Condensed",sans-serif;color:var(--ink)}
  .front-credit .publisher{font-size:15px;margin-bottom:12px}
  .front-credit .author{color:var(--author-orange);font-family:"Oswald",sans-serif;font-weight:500;font-size:19px;line-height:20px}
  .front-credit .role{font-size:15px;margin-top:2px}
  .front-brand{left:1000px;top:604px;font-size:28px}
</style>
</head>
<body>
<main class="spread">

  <!-- back cover -->
  <section class="back-cover">
    <svg class="abs back-wave" width="560" height="220" viewBox="0 0 560 220" aria-hidden="true">
      <path d="M0 0H548Q440 105 200 142Q70 165 0 215Z" fill="var(--teal)"/>
    </svg>
    <div class="abs back-icon" role="img" aria-label="Calendar with magnifying glass illustration"></div>
    <h2 class="abs back-title">SUMMIT<br>BLUEPRINTS</h2>
    <svg class="abs back-play" viewBox="0 0 42 38" aria-hidden="true"><path d="M15 9L30 19L15 29Z" fill="#fff"/></svg>
    <div class="abs back-label">
      <p class="sub">BEST PRACTICES FOR SCHEDULING<br>REAL-WORLD PROGRAMS</p>
      <p class="subsub">Screenshots in Ganttwise Studio</p>
    </div>
    <div class="abs back-box"></div>
    <div class="abs brand back-brand"><span>Brindlex</span><span class="dot"></span></div>
  </section>

  <!-- spine -->
  <section class="abs spine">
    <div class="spine-text">
      <p class="spine-title">SUMMIT BLUEPRINTS</p>
      <p class="spine-sub">BEST PRACTICES FOR SCHEDULING REAL-WORLD PROGRAMS <span>Screenshots in Ganttwise Studio</span></p>
      <p class="spine-author">Maren Oltvik, CSP, Ganttwise Expert</p>
    </div>
    <div class="brand spine-brand"><span>Brindlex</span></div>
    <div class="spine-badge"></div>
  </section>

  <!-- front cover -->
  <section class="front-cover">
    <svg class="abs front-circle" width="564" height="693" viewBox="0 0 564 693" aria-hidden="true">
      <circle cx="310" cy="600" r="310" fill="var(--teal)"/>
      <circle cx="300" cy="510" r="170" fill="none" stroke="#fff" stroke-width="2" stroke-dasharray="6 8" opacity=".7"/>
      <circle cx="300" cy="510" r="220" fill="none" stroke="#fff" stroke-width="2" opacity=".5"/>
    </svg>
    <h1 class="abs front-title">SUMMIT<br>BLUEPRINTS</h1>
    <svg class="abs front-play" viewBox="0 0 98 88" aria-hidden="true"><path d="M34 20L70 44L34 68Z" fill="#fff"/></svg>
    <div class="abs front-label">
      <p class="sub">BEST PRACTICES FOR SCHEDULING<br>REAL-WORLD PROGRAMS</p>
      <p class="subsub">Screenshots in Ganttwise Studio</p>
    </div>
    <div class="abs front-art" role="img" aria-label="Schedule grid with a calendar and magnifying glass illustration"></div>
    <div class="abs front-credit">
      <p class="publisher">Published by Brindlex Corporation</p>
      <p class="author">Maren Oltvik, CSP,<br>Ganttwise Expert</p>
      <p class="role">President Brindlex Corporation</p>
    </div>
    <div class="abs brand front-brand"><span>Brindlex</span><span class="dot"></span></div>
  </section>

</main>
</body>
</html>
```